RICE AND RUN WALL POSTER

Hi designer,

I would like to create a poster to put on my wall.

My intention is to place a bicycle onto a wall and have these words vinyl stick next to it.

" Life is not a race.
It is a journey
Enjoy each moment. Relax!
Have a bowl of Rice and Run
Make all your dreams come true "

I like traditional fonts - easy to read. See example. This is something I would love.

It will be on a white wall so black text would be ok. I have also attached my logo - maybe try include Rice and Run font in your design if possible - but not important.

Good luck everyone.

Font styles to use
Decorative
Script

Requirements
Must have
• The placement of my bike will be on the top left corner of the wall so I think it will be best fit if all designs are done in horizontal rectangular shape (landscape)

```html
<!DOCTYPE html>
<html lang="en">
<head>
<meta charset="utf-8">
<title>Rice and Run – Wall Poster</title>
<link rel="stylesheet" href="https://fonts.googleapis.com/css2?family=Kaushan+Script&family=Allura&family=Caveat:wght@500&family=Dancing+Script&display=swap">
<style>
  :root {
    --page: #ffffff;
    --concrete-light: #7d8ea3;
    --concrete-mid: #6a7b91;
    --concrete-dark: #56667b;
    --ink-white: #ececec;
    --ink-yellow: #d6d43a;
    --ink-maroon: #7a1f4c;
    --ink-purple: #b77ee8;
    --ink-cyan: #5ee3de;
    --ink-teal: #4fc6cf;
    --ink-pink: #e07ab5;
    --ink-lime: #c6cc3b;
    --quote-mark: #0a0a0a;
  }
  html, body {
    margin: 0;
    padding: 0;
    width: 1200px;
    height: 1000px;
    overflow: hidden;
    background: var(--page);
  }
  .poster { display: block; width: 1200px; height: 1000px; }
  .brush { font-family: "Kaushan Script", cursive; }
  .fine-script { font-family: "Allura", cursive; }
  .hand { font-family: "Caveat", cursive; font-weight: 500; }
  .small-script { font-family: "Dancing Script", cursive; }
  .quote-mark { fill: var(--quote-mark); }
  .w-life, .w-small, .w-it, .w-a, .w-moment, .w-bowl, .w-brand { fill: var(--ink-white); }
  .w-not { fill: var(--ink-yellow); }
  .w-race { fill: var(--ink-maroon); }
  .w-is { fill: var(--ink-purple); }
  .w-journey { fill: var(--ink-cyan); }
  .w-relax { fill: var(--ink-lime); }
  .w-enjoy { fill: var(--ink-pink); }
  .w-dreams { fill: var(--ink-teal); }
  .rule-yellow { stroke: var(--ink-yellow); stroke-width: 2; }
  .rule-cyan { stroke: var(--ink-cyan); stroke-width: 2; }
</style>
</head>
<body>
<svg class="poster" viewBox="0 0 1200 1000" xmlns="http://www.w3.org/2000/svg">
  <defs>
    <linearGradient id="concrete" x1="0" y1="0" x2="1" y2="1">
      <stop offset="0" stop-color="var(--concrete-dark)"/>
      <stop offset="0.5" stop-color="var(--concrete-light)"/>
      <stop offset="1" stop-color="var(--concrete-mid)"/>
    </linearGradient>
  </defs>

  <rect class="backdrop" x="29" y="262" width="1142" height="454" fill="url(#concrete)"
        role="img" aria-label="Photograph of cracked blue-grey concrete wall texture"/>

  <g class="quote">
    <g class="quote-open">
      <path class="quote-mark" d="M126 290 L146 284 L142 340 L130 346 Z"/>
      <path class="quote-mark" d="M156 284 L180 278 L172 334 L160 340 Z"/>
    </g>

    <text class="brush w-life" x="183" y="360" font-size="100">LIFE</text>
    <text class="brush w-small" x="430" y="328" font-size="28">is</text>
    <text class="brush w-not" x="458" y="388" font-size="96">NOT</text>
    <text class="brush w-small" x="658" y="338" font-size="30">a</text>
    <text class="brush w-race" x="688" y="390" font-size="112">RACE...</text>
    <line class="rule-yellow" x1="705" y1="408" x2="1065" y2="408"/>

    <text class="brush w-it" x="226" y="458" font-size="52">it</text>
    <text class="brush w-is" x="266" y="490" font-size="50">is</text>
    <text class="brush w-a" x="318" y="484" font-size="72">A</text>
    <text class="brush w-journey" x="368" y="508" font-size="108">journey.</text>

    <text class="fine-script w-relax" x="805" y="545" font-size="112">Relax!</text>

    <text class="fine-script w-enjoy" x="88" y="588" font-size="132">Enjoy</text>
    <text class="brush w-moment" x="380" y="590" font-size="44">each moment...</text>
    <line class="rule-cyan" x1="100" y1="605" x2="650" y2="605"/>

    <text class="small-script w-bowl" x="950" y="582" font-size="22">Have a bowl of</text>
    <text class="brush w-brand" x="815" y="628" font-size="36">Rice and Run</text>

    <g class="quote-close">
      <path class="quote-mark" d="M1090 592 L1110 586 L1108 642 L1096 648 Z"/>
      <path class="quote-mark" d="M1122 598 L1144 592 L1146 652 L1134 658 Z"/>
    </g>

    <text class="hand w-dreams" x="325" y="692" font-size="50">Make all your dreams come true</text>
  </g>
</svg>
</body>
</html>
```